Ridgewell Stonecraft Construction Needs business card

Hey we are in need of business card designs. I have upload our logo as a guideline, but free feel to run with it or come up with something unique.
Pls have fun with it and be creative. the name says it all!
i will give some directions after i see a few entries..
Logo source file has been uploaded..
Hey because of the logo is so colourful already.
Can we have a few submissions with less colour.
Also we are looking for clever/hidden/descriptive business card.

```html
<!DOCTYPE html>
<html lang="en">
<head>
<meta charset="utf-8">
<title>Ridgewell Stonecraft Construction – Business Card</title>
<link rel="stylesheet" href="https://fonts.googleapis.com/css2?family=Exo+2:wght@500;600&family=Open+Sans:wght@400;600&display=swap">
<style>
  :root {
    --bg: #ece9e4;
    --card-white: #ffffff;
    --card-blue: #1a8fd6;
    --ink-dark: #2e2e2e;
    --ink-grey: #5f6368;
    --ink-soft: #7a7a7a;
    --icon-green: #2a9d4a;
    --rule-blue: #1a8fd6;
  }
  * { box-sizing: border-box; margin: 0; padding: 0; }
  html, body {
    width: 1200px; height: 672px; overflow: hidden;
    background: var(--bg);
  }
  .stage {
    width: 1200px; height: 672px;
    display: flex; align-items: center; justify-content: center; gap: 80px;
  }
  .card {
    width: 320px; height: 560px;
    border-radius: 2px;
    box-shadow: 0 6px 20px rgba(0,0,0,0.12);
    position: relative;
  }
  .card--front { background: var(--card-white); }
  .card--back { background: var(--card-blue); }

  .brand {
    position: absolute; top: 92px; left: 34px; right: 34px;
    display: flex; align-items: center; gap: 12px;
  }
  .brand__square {
    width: 34px; height: 34px; flex: none;
    background: var(--ink-grey);
  }
  .brand__name {
    font-family: "Exo 2", sans-serif; font-weight: 600;
    font-size: 21px; line-height: 1.1;
    color: var(--ink-grey); text-transform: uppercase; letter-spacing: 0.5px;
  }
  .brand__rule {
    position: absolute; top: 170px; left: 34px; right: 34px;
    height: 3px; background: var(--rule-blue);
  }

  .person { position: absolute; top: 262px; left: 34px; }
  .person__name {
    font-family: "Exo 2", sans-serif; font-weight: 600;
    font-size: 24px; color: var(--ink-dark); letter-spacing: 1px;
  }
  .person__role {
    font-family: "Open Sans", sans-serif; font-weight: 600;
    font-size: 10px; color: var(--ink-soft); letter-spacing: 1px; margin-top: 2px;
  }

  .contacts {
    position: absolute; top: 338px; left: 34px; right: 24px;
    list-style: none;
  }
  .contacts__item {
    display: flex; align-items: flex-start; gap: 10px;
    font-family: "Open Sans", sans-serif; font-size: 11.5px;
    color: var(--ink-dark); margin-bottom: 11px; line-height: 20px;
  }
  .contacts__icon {
    width: 20px; height: 20px; flex: none;
    background: var(--icon-green); border-radius: 2px;
    display: flex; align-items: center; justify-content: center;
  }
  .contacts__icon svg { width: 13px; height: 13px; fill: #fff; }
  .contacts__text--address { line-height: 15px; padding-top: 2px; }
</style>
</head>
<body>
<main class="stage">
  <section class="card card--front" aria-label="Business card front">
    <div class="brand">
      <span class="brand__square"></span>
      <span class="brand__name">Ridgewell Stonecraft Construction</span>
    </div>
    <div class="brand__rule"></div>

    <div class="person">
      <p class="person__name">DANIEL MARSH</p>
      <p class="person__role">GENERAL MANAGER</p>
    </div>

    <ul class="contacts">
      <li class="contacts__item">
        <span class="contacts__icon"><svg viewBox="0 0 16 16"><path d="M4 1h3l1 4-2 1.5a8 8 0 0 0 3.5 3.5L11 8l4 1v3c0 1-1 2-2 2C7 14 2 9 2 3c0-1 1-2 2-2z"/></svg></span>
        <span>014 672 3058</span>
      </li>
      <li class="contacts__item">
        <span class="contacts__icon"><svg viewBox="0 0 16 16"><path d="M3 5h10v8H3z M5 2h6v3H5z"/><rect x="5" y="7" width="6" height="1.5" fill="#2a9d4a"/></svg></span>
        <span>014 672 3091</span>
      </li>
      <li class="contacts__item">
        <span class="contacts__icon"><svg viewBox="0 0 16 16"><path d="M1 3h14v10H1z"/><path d="M1 3l7 6 7-6" fill="none" stroke="#2a9d4a" stroke-width="1.5"/></svg></span>
        <span>d.marsh@ridgewellmail.com</span>
      </li>
      <li class="contacts__item">
        <span class="contacts__icon"><svg viewBox="0 0 16 16"><circle cx="8" cy="8" r="6.5" fill="none" stroke="#fff" stroke-width="1.4"/><path d="M1.5 8h13M8 1.5c-3 3-3 10 0 13M8 1.5c3 3 3 10 0 13" fill="none" stroke="#fff" stroke-width="1.2"/></svg></span>
        <span>www.ridgewellstone.com</span>
      </li>
      <li class="contacts__item">
        <span class="contacts__icon"><svg viewBox="0 0 16 16"><path d="M8 1a5 5 0 0 1 5 5c0 4-5 9-5 9S3 10 3 6a5 5 0 0 1 5-5z"/><circle cx="8" cy="6" r="2" fill="#2a9d4a"/></svg></span>
        <span class="contacts__text--address">27 Quarry Lane, Suite 4,<br>Harrow Vale</span>
      </li>
    </ul>
  </section>

  <section class="card card--back" aria-label="Business card back"></section>
</main>
</body>
</html>
```